label bath salt on glass bottle

for our bath salts (Flavours Rose, Lavender, Lemongras, mountain herbs, Mint, Cashmere) we need a label in the size of 50mm height an 55mm wide.

Target Market(s)

Prestige stores

Font styles to use
Serif
Script

Colors

Designer to choose colors to be used in the design.

Requirements
Must have
• Name of the label:
• Headline: Badesalz (can be also written in two words) Bade Salz
• Describtion of the sel: Totes Meer (comes from Dead Sea)
• Name of the different fragrances:
• Rose
• Pfingstrose (Peony)
• Lemongras
• Alpenkräuter (mountain herbs)
• Minze (mint)
• Cashmere
• Lavendel (lavender)
Nice to have
• Made with love in Switzerland
• Logos:
• Use our LOGO in the attachment or just
• FENIVU
• Switzerland

```html
<!DOCTYPE html>
<html lang="de">
<head>
<meta charset="utf-8">
<title>Bade Salz – Etiketten</title>
<link rel="stylesheet" href="https://fonts.googleapis.com/css2?family=Montserrat:wght@400;500&family=Playfair+Display:ital,wght@1,400&family=Yellowtail&display=swap">
<style>
  :root {
    --page-bg: #ffffff;
    --frame: #222222;
    --gold: #c4ad88;
    --band: #ec7d75;
    --band-dark: #df6c66;
    --band-light: #f28a80;
    --cross: #f6f6f4;
    --title-fill: #b59f7e;
    --title-stroke: #3a3128;
    --subtitle: #333333;
    --rose: #ff3366;
    --peony: #ff1ae8;
    --lemongrass: #86f23a;
    --herbs: #5cff66;
    --mint: #5dff24;
    --cashmere: #f98a0c;
    --lavender: #9b3ff2;
    --pill-text: #ffffff;
  }
  html, body { margin: 0; padding: 0; overflow: hidden; }
  body { width: 1082px; height: 1200px; background: var(--page-bg); }
  .sheet {
    position: relative; width: 1082px; height: 1200px; box-sizing: border-box;
    border: 1.5px solid var(--frame); background: var(--page-bg);
  }
  .label {
    position: absolute; width: 312px; height: 342px; box-sizing: border-box;
    border: 1.5px solid var(--frame); background: #fff; overflow: hidden;
  }
  .label__head { position: absolute; left: 0; top: 0; width: 100%; height: 125px; }
  .brand {
    position: absolute; left: 0; width: 100%; top: 34px; text-align: center;
    font-family: "Montserrat", sans-serif; font-weight: 500; font-size: 25px;
    letter-spacing: 2px; color: var(--gold);
  }
  .tagline {
    position: absolute; left: 0; width: 100%; top: 97px; text-align: center;
    font-family: "Playfair Display", serif; font-style: italic; font-size: 15px;
    color: var(--gold); letter-spacing: 0.5px;
  }
  .label__band {
    position: absolute; left: 0; top: 125px; width: 100%; height: 217px;
    background: linear-gradient(160deg, var(--band-dark) 0%, var(--band-light) 35%, var(--band) 60%, var(--band-dark) 80%, var(--band-light) 100%);
  }
  .cross { position: absolute; background: var(--cross); }
  .cross--v { left: 139px; top: 32px; width: 34px; height: 116px; }
  .cross--h { left: 97px; top: 73px; width: 117px; height: 34px; }
  .title {
    position: absolute; left: 0; width: 100%; top: 18px; text-align: center;
    font-family: "Yellowtail", cursive; font-size: 52px; line-height: 1;
    color: var(--title-fill); -webkit-text-stroke: 1.6px var(--title-stroke);
  }
  .subtitle {
    position: absolute; left: 0; width: 100%; top: 70px; text-align: center;
    font-family: "Montserrat", sans-serif; font-size: 26px; line-height: 1; color: var(--subtitle);
  }
  .ornament {
    position: absolute; top: 146px; width: 39px; height: 53px;
    border-radius: 18px; background: rgba(255,255,255,0.18);
  }
  .ornament--left { left: 6px; }
  .ornament--right { right: 6px; }
  .flavour {
    position: absolute; left: 49px; top: 159px; width: 213px; height: 28px;
    border-radius: 14px; display: flex; align-items: center; justify-content: center;
    font-family: "Montserrat", sans-serif; font-weight: 500; font-size: 19px;
    color: var(--pill-text);
  }
  .flavour--small { font-size: 12px; }
  .flavour--rose { background: var(--rose); }
  .flavour--peony { background: var(--peony); }
  .flavour--lemongrass { background: var(--lemongrass); }
  .flavour--herbs { background: var(--herbs); }
  .flavour--mint { background: var(--mint); }
  .flavour--cashmere { background: var(--cashmere); }
  .flavour--lavender { background: var(--lavender); }
</style>
</head>
<body>
<main class="sheet">

  <section class="label" style="left:42px; top:47px;">
    <div class="label__head"><div class="brand">FENIVU</div><div class="tagline">moments of calm</div></div>
    <div class="label__band" role="img" aria-label="Red silk fabric background">
      <div class="cross cross--v"></div><div class="cross cross--h"></div>
      <div class="title">Bade Salz</div><div class="subtitle">Totes Meer</div>
      <div class="ornament ornament--left" role="img" aria-label="Scroll ornament"></div>
      <div class="ornament ornament--right" role="img" aria-label="Scroll ornament"></div>
      <div class="flavour flavour--rose">Rose</div>
    </div>
  </section>

  <section class="label" style="left:385px; top:47px;">
    <div class="label__head"><div class="brand">FENIVU</div><div class="tagline">moments of calm</div></div>
    <div class="label__band" role="img" aria-label="Red silk fabric background">
      <div class="cross cross--v"></div><div class="cross cross--h"></div>
      <div class="title">Bade Salz</div><div class="subtitle">Totes Meer</div>
      <div class="ornament ornament--left" role="img" aria-label="Scroll ornament"></div>
      <div class="ornament ornament--right" role="img" aria-label="Scroll ornament"></div>
      <div class="flavour flavour--peony" style="font-size:17px;">Pfingstrose</div>
    </div>
  </section>

  <section class="label" style="left:728px; top:47px;">
    <div class="label__head"><div class="brand">FENIVU</div><div class="tagline">moments of calm</div></div>
    <div class="label__band" role="img" aria-label="Red silk fabric background">
      <div class="cross cross--v"></div><div class="cross cross--h"></div>
      <div class="title">Bade Salz</div><div class="subtitle">Totes Meer</div>
      <div class="ornament ornament--left" role="img" aria-label="Scroll ornament"></div>
      <div class="ornament ornament--right" role="img" aria-label="Scroll ornament"></div>
      <div class="flavour flavour--lemongrass">lemongrass</div>
    </div>
  </section>

  <section class="label" style="left:385px; top:429px;">
    <div class="label__head"><div class="brand">FENIVU</div><div class="tagline">moments of calm</div></div>
    <div class="label__band" role="img" aria-label="Red silk fabric background">
      <div class="cross cross--v"></div><div class="cross cross--h"></div>
      <div class="title">Bade Salz</div><div class="subtitle">Totes Meer</div>
      <div class="ornament ornament--left" role="img" aria-label="Scroll ornament"></div>
      <div class="ornament ornament--right" role="img" aria-label="Scroll ornament"></div>
      <div class="flavour flavour--herbs flavour--small">Alpenkrauter</div>
    </div>
  </section>

  <section class="label" style="left:42px; top:811px;">
    <div class="label__head"><div class="brand">FENIVU</div><div class="tagline">moments of calm</div></div>
    <div class="label__band" role="img" aria-label="Red silk fabric background">
      <div class="cross cross--v"></div><div class="cross cross--h"></div>
      <div class="title">Bade Salz</div><div class="subtitle">Totes Meer</div>
      <div class="ornament ornament--left" role="img" aria-label="Scroll ornament"></div>
      <div class="ornament ornament--right" role="img" aria-label="Scroll ornament"></div>
      <div class="flavour flavour--mint">Minze</div>
    </div>
  </section>

  <section class="label" style="left:385px; top:811px;">
    <div class="label__head"><div class="brand">FENIVU</div><div class="tagline">moments of calm</div></div>
    <div class="label__band" role="img" aria-label="Red silk fabric background">
      <div class="cross cross--v"></div><div class="cross cross--h"></div>
      <div class="title">Bade Salz</div><div class="subtitle">Totes Meer</div>
      <div class="ornament ornament--left" role="img" aria-label="Scroll ornament"></div>
      <div class="ornament ornament--right" role="img" aria-label="Scroll ornament"></div>
      <div class="flavour flavour--cashmere">Cashmere</div>
    </div>
  </section>

  <section class="label" style="left:728px; top:811px;">
    <div class="label__head"><div class="brand">FENIVU</div><div class="tagline">moments of calm</div></div>
    <div class="label__band" role="img" aria-label="Red silk fabric background">
      <div class="cross cross--v"></div><div class="cross cross--h"></div>
      <div class="title">Bade Salz</div><div class="subtitle">Totes Meer</div>
      <div class="ornament ornament--left" role="img" aria-label="Scroll ornament"></div>
      <div class="ornament ornament--right" role="img" aria-label="Scroll ornament"></div>
      <div class="flavour flavour--lavender">Lavendel</div>
    </div>
  </section>

</main>
</body>
</html>
```